Granite Surface Works, Inc. Business Card

New business, we do epoxy, polishing concrete, underlayment, fluid applied flooring, sound proofing, double sided, will need 3 sets of cards with 3 different names and phone numbers.
Company: Granite Surface Works, Inc.
Address and Phone: 6339 Charlotte Pike PMB 2183Nashville, TN 37209
(615) 384-7190
www.granitesurfaceworks.example

Target Market(s)

General Contractors, Contractors, Architects

Contact Information for Business Card

1st Card: Derek Halvorsen C. 708.214.8573 e. derek@granitesurfaceworks.example
Vice President
2nd Card: Morgan Brasfield C. 708.361.5847 e. morgan@granitesurfaceworks.example
President
3rd Card: Raj Oti C. 405.617.3328 e. raj@granitesurfaceworks.example
Managing Partner

Font styles to use
Serif
Sans Serif

Requirements
Must have
• Professional Clean Design, Implement colors from Logo or nicely contrasting
Nice to have
• N/A

```html
<!DOCTYPE html>
<html lang="en">
<head>
<meta charset="utf-8">
<title>Granite Surface Works, Inc. Business Card</title>
<link href="https://fonts.googleapis.com/css2?family=Montserrat:wght@500;600;700&family=Roboto:wght@400&display=swap" rel="stylesheet">
<style>
  :root{
    --stage:#2b2b2d;
    --card-dark:#3a3638;
    --card-light:#ffffff;
    --brand-blue:#2f74c0;
    --band-blue:#1f5fb8;
    --brand-green:#5ea146;
    --text-gray:#555555;
    --rule:#8a8a8a;
  }
  *{box-sizing:border-box;margin:0;padding:0}
  html,body{width:1200px;height:929px;overflow:hidden}
  body{background:var(--stage);position:relative;font-family:'Roboto',sans-serif}
  .card{position:absolute;width:600px;height:343px;box-shadow:0 10px 30px rgba(0,0,0,.45)}
  .card-back{left:300px;top:70px;background:var(--card-dark);display:flex;align-items:center;justify-content:center}
  .card-front{left:300px;top:490px;background:var(--card-light);overflow:hidden}
  .wordmark{display:flex;align-items:center;gap:14px;font-family:'Montserrat',sans-serif;font-weight:700;letter-spacing:.5px}
  .wordmark .mark{width:22px;height:22px;background:var(--brand-green);flex:none}
  .card-back .wordmark{color:#ffffff;font-size:30px}
  .card-front .wordmark{position:absolute;right:34px;top:48px;color:#2e2c2d;font-size:21px}
  .divider{position:absolute;left:270px;right:34px;top:112px;height:1px;background:var(--rule)}
  .person{position:absolute;left:40px;top:150px;font-family:'Montserrat',sans-serif}
  .person-name{color:var(--brand-blue);font-weight:700;font-size:20px;text-transform:uppercase;letter-spacing:.3px}
  .person-title{color:var(--brand-green);font-weight:600;font-size:17px;margin-top:2px}
  .contact{position:absolute;left:40px;top:218px;list-style:none}
  .contact li{display:flex;align-items:center;gap:9px;color:var(--text-gray);font-size:14.5px;line-height:23px}
  .contact svg{width:14px;height:14px;flex:none}
  .company{position:absolute;right:34px;top:140px;text-align:right}
  .company-name{color:var(--brand-blue);font-family:'Roboto',sans-serif;font-size:17px}
  .company-address{color:var(--text-gray);font-size:15px;line-height:21px;margin-top:2px}
  .band{position:absolute;left:0;bottom:0;width:600px;height:32px}
</style>
</head>
<body>
  <section class="card card-back" aria-label="Card back">
    <div class="wordmark"><span class="mark"></span>Granite Surface Works</div>
  </section>

  <section class="card card-front" aria-label="Card front">
    <div class="wordmark"><span class="mark"></span>Granite Surface Works</div>
    <div class="divider"></div>

    <div class="person">
      <p class="person-name">Derek Halvorsen</p>
      <p class="person-title">Vice President</p>
    </div>

    <ul class="contact">
      <li><svg viewBox="0 0 24 24"><path fill="#1f5fb8" d="M6.6 10.8a15 15 0 0 0 6.6 6.6l2.2-2.2c.3-.3.7-.4 1-.2 1.1.4 2.3.6 3.6.6.6 0 1 .4 1 1V20c0 .6-.4 1-1 1A17 17 0 0 1 3 4c0-.6.4-1 1-1h3.5c.6 0 1 .4 1 1 0 1.3.2 2.5.6 3.6.1.3 0 .7-.2 1z"/></svg>708.214.8573</li>
      <li><svg viewBox="0 0 24 24"><rect x="2" y="5" width="20" height="14" fill="#1f5fb8"/><path d="M2 5l10 8 10-8" fill="none" stroke="#fff" stroke-width="1.6"/></svg>derek@granitesurfaceworks.example</li>
      <li><svg viewBox="0 0 24 24"><circle cx="12" cy="12" r="9" fill="none" stroke="#1f5fb8" stroke-width="2"/><path d="M3 12h18M12 3c3 3 3 15 0 18M12 3c-3 3-3 15 0 18" fill="none" stroke="#1f5fb8" stroke-width="1.6"/></svg>www.granitesurfaceworks.example</li>
    </ul>

    <div class="company">
      <p class="company-name">Granite Surface Works, Inc.</p>
      <p class="company-address">4817 Willowmere Road<br>PMB 5046 Nashville, TN 37299</p>
    </div>

    <svg class="band" viewBox="0 0 600 32" preserveAspectRatio="none" aria-hidden="true">
      <polygon points="0,14 410,14 404,32 0,32" fill="var(--band-blue)"/>
      <polygon points="418,0 600,0 600,32 410,32" fill="var(--brand-green)"/>
    </svg>
  </section>
</body>
</html>
```